Business cards, letter head, stationery
trial lawyer
Bright & Fun-filled
Teodoro Villaseca
Trial Lawyer
2716 kelverham, suite 300
Bellaire Texas 77538
Tevmilux@quarnela.com
Need to include:
Offices in Houston , San Antonio, and eagle pass Texas
Use winning logo

```html
<!DOCTYPE html>
<html lang="en">
<head>
<meta charset="utf-8">
<title>Teodoro Villaseca – Business Card</title>
<link href="https://fonts.googleapis.com/css2?family=Open+Sans:wght@400;600;700&display=swap" rel="stylesheet">
<style>
  :root{
    --royal:#2f36b6;
    --sky:#22b8ee;
    --sun:#ffb42e;
    --paper:#ffffff;
    --backdrop:#eef1f8;
    --ink:#1b1c2c;
  }
  *{box-sizing:border-box;margin:0;padding:0}
  html,body{width:1200px;height:1042px;overflow:hidden}
  body{background:var(--backdrop);font-family:"Open Sans",Arial,sans-serif;color:var(--ink);position:relative}
  .card{position:absolute;left:230px;width:740px;height:420px;background:var(--paper);border-radius:42px;overflow:hidden;box-shadow:0 6px 18px rgba(20,30,80,.18)}
  .card--front{top:80px}
  .card--back{top:560px}
  .card__wave{position:absolute;left:0;top:0;width:740px;height:420px}
  .brand{position:absolute;right:44px;top:40px;display:flex;align-items:flex-start;gap:12px}
  .brand__mark{width:54px;height:54px;background:var(--royal);flex:none}
  .brand__text{color:var(--royal)}
  .brand__name{font-weight:600;font-size:27px;letter-spacing:1.5px;text-transform:uppercase;line-height:1.05}
  .brand__title{font-weight:600;font-size:17px;letter-spacing:3px;text-transform:uppercase;margin-top:4px;padding-bottom:4px;border-bottom:1.5px solid var(--royal)}
  .brand__tag{font-weight:600;font-size:11px;margin-top:4px}
  .person{position:absolute;left:56px;top:148px}
  .person__name{font-weight:700;font-size:22px;line-height:1.2}
  .person__role{font-weight:600;font-size:15px;margin-left:78px}
  .contact{position:absolute;left:56px;top:334px;color:#fff;font-size:11.5px;line-height:1.55}
  .contact__row{display:flex}
  .contact__item{padding-right:26px;margin-right:26px;border-right:1px solid rgba(255,255,255,.6)}
  .contact__item:last-child{border-right:none}
  .offices{position:absolute;left:0;right:0;bottom:34px;text-align:center;color:#fff;font-weight:600;font-size:13px;letter-spacing:1.5px;text-transform:uppercase}
  .offices__dot{color:var(--sun);margin:0 10px}
</style>
</head>
<body>
  <section class="card card--front">
    <svg class="card__wave" viewBox="0 0 740 420" aria-hidden="true">
      <path d="M0 300 C170 300 300 330 420 322 C560 310 660 262 740 228 L740 420 L0 420 Z" fill="var(--royal)"/>
      <path d="M300 326 C450 326 590 284 740 216 L740 228 C610 288 450 328 300 326 Z" fill="var(--sky)"/>
    </svg>
    <div class="brand">
      <div class="brand__mark"></div>
      <div class="brand__text">
        <div class="brand__name">Teodoro Villaseca</div>
        <div class="brand__title">Attorney at Law</div>
        <div class="brand__tag">A Professional Corporation</div>
      </div>
    </div>
    <div class="person">
      <div class="person__name">Teodoro Villaseca</div>
      <div class="person__role">Trial Lawyer</div>
    </div>
    <div class="contact">
      <div>2716 kelverham, suite 300, Bellaire Texas 77538</div>
      <div class="contact__row">
        <span class="contact__item">Phone: 713-555-0148</span>
        <span class="contact__item">Cell: 210-555-0193</span>
        <span class="contact__item">Fax: 713-555-0172</span>
      </div>
      <div>Email: Tevmilux@quarnela.com</div>
    </div>
  </section>

  <section class="card card--back">
    <svg class="card__wave" viewBox="0 0 740 420" aria-hidden="true">
      <path d="M0 262 C170 262 300 296 420 288 C560 276 660 228 740 196 L740 420 L0 420 Z" fill="var(--royal)"/>
      <path d="M300 292 C450 292 590 250 740 184 L740 196 C610 254 450 294 300 292 Z" fill="var(--sky)"/>
    </svg>
    <div class="brand">
      <div class="brand__mark"></div>
      <div class="brand__text">
        <div class="brand__name">Teodoro Villaseca</div>
        <div class="brand__title">Attorney at Law</div>
        <div class="brand__tag">A Professional Corporation</div>
      </div>
    </div>
    <div class="offices">Houston<span class="offices__dot">●</span>San Antonio<span class="offices__dot">●</span>Eagle Pass, Texas</div>
  </section>
</body>
</html>
```